Tolver Performance Bold Comet Multi Vitamin Label Design

We need a label design for our Sports Performance Daily Multi Vitamin specially created and branded for our Tolver Performance line for the University of Ostrander. The feel is edgy, sports nutrition. Two logos need to be incorporated... Tolver and the Collective Logo attached. The colors should be the official colors of the University of Ostrander. The font may also be the Georgia font... or the Tolver font. Or any font. A hydration product will also be created later on...so this label design may be used on many products. Please utilize the collective logo similar to the use in the attached photo. No official trademark items from the University of Ostrander should be used. Attached is also an image if the bottle (white) that will be used for the vitamin. Please use red, black, grey, white. We are looking for the front design only right now and once selected, will work on the nutrition/back label portion with the artist.

```html
<!DOCTYPE html>
<html lang="en">
<head>
<meta charset="utf-8">
<title>Tolver Performance Multi Vitamin Label</title>
<link rel="stylesheet" href="https://fonts.googleapis.com/css2?family=Montserrat:wght@600;800&display=swap">
<style>
  :root {
    --backdrop: #181818;
    --label-white: #ffffff;
    --ink-black: #0d0d0d;
    --grit-grey: #3a3a3a;
    --team-red: #e3141c;
    --text-dark: #1c1c1c;
  }
  html, body {
    margin: 0;
    padding: 0;
    width: 1200px;
    height: 1200px;
    overflow: hidden;
    background: var(--backdrop);
  }
  .canvas {
    position: relative;
    width: 1200px;
    height: 1200px;
  }
  .label {
    position: absolute;
    left: 80px;
    top: 151px;
    width: 1040px;
    height: 898px;
    background: var(--label-white);
    overflow: hidden;
  }
  .grit-band {
    position: absolute;
    left: 0;
    width: 100%;
  }
  .grit-band--top { top: 0; height: 190px; }
  .grit-band--bottom { bottom: 0; height: 170px; }
  .grit-band svg { display: block; width: 100%; height: 100%; }
  .collective-mark {
    position: absolute;
    left: 240px;
    top: 190px;
    display: flex;
    align-items: center;
    gap: 10px;
    font-family: 'Montserrat', sans-serif;
    font-weight: 800;
    font-size: 18px;
    letter-spacing: 1px;
    color: var(--ink-black);
    text-transform: uppercase;
  }
  .collective-mark .dot {
    width: 18px;
    height: 18px;
    border-radius: 50%;
    background: var(--team-red);
  }
  .brand-mark {
    position: absolute;
    left: 0;
    width: 100%;
    top: 300px;
    text-align: center;
    font-family: 'Montserrat', sans-serif;
    font-weight: 800;
    font-size: 96px;
    letter-spacing: 4px;
    color: var(--ink-black);
    text-transform: uppercase;
    line-height: 1;
  }
  .performance-band {
    position: absolute;
    left: 230px;
    top: 462px;
    width: 550px;
    height: 66px;
    background: var(--team-red);
    display: flex;
    align-items: center;
    justify-content: center;
  }
  .performance-band span {
    font-family: 'Montserrat', sans-serif;
    font-weight: 800;
    font-size: 46px;
    letter-spacing: 2px;
    color: var(--label-white);
    text-transform: uppercase;
  }
  .product-name {
    position: absolute;
    left: 0;
    width: 100%;
    top: 578px;
    text-align: center;
    font-family: 'Montserrat', sans-serif;
    font-weight: 600;
    font-size: 29px;
    letter-spacing: 3px;
    color: var(--text-dark);
    text-transform: uppercase;
  }
</style>
</head>
<body>
<main class="canvas">
  <section class="label">
    <div class="grit-band grit-band--top" role="img" aria-label="Black distressed grunge edge texture along the top of the label">
      <svg viewBox="0 0 1040 190" preserveAspectRatio="none">
        <defs>
          <linearGradient id="gritTop" x1="0" y1="0" x2="0" y2="1">
            <stop offset="0" stop-color="#0d0d0d"/>
            <stop offset="0.8" stop-color="#0d0d0d"/>
            <stop offset="1" stop-color="#3a3a3a"/>
          </linearGradient>
        </defs>
        <path d="M0 0H1040V150L1000 140L920 160L840 110L760 150L680 105L600 140L520 95L440 135L360 105L280 150L200 120L120 160L60 130L0 160Z" fill="url(#gritTop)"/>
      </svg>
    </div>

    <div class="collective-mark"><span class="dot"></span>Harrow Collective</div>

    <div class="brand-mark">Tolver</div>

    <div class="performance-band"><span>Performance</span></div>

    <div class="product-name">Multi Vitamin</div>

    <div class="grit-band grit-band--bottom" role="img" aria-label="Black distressed grunge edge texture along the bottom of the label">
      <svg viewBox="0 0 1040 170" preserveAspectRatio="none">
        <defs>
          <linearGradient id="gritBottom" x1="0" y1="1" x2="0" y2="0">
            <stop offset="0" stop-color="#0d0d0d"/>
            <stop offset="0.8" stop-color="#0d0d0d"/>
            <stop offset="1" stop-color="#3a3a3a"/>
          </linearGradient>
        </defs>
        <path d="M0 170H1040V0L980 40L900 70L820 50L740 90L660 60L580 95L500 70L420 100L340 80L260 110L180 75L100 115L40 100L0 120Z" fill="url(#gritBottom)"/>
      </svg>
    </div>
  </section>
</main>
</body>
</html>
```